Allied Health Clinic needs catchy poster ad for lightbox

We need a catchy and effective poster designed for our retail lightbox which is in a busy corridor. We are a multi disciplinary sports injury clinic offering a range of allied health services. Established in 1999. We need people to understand our business identity and services clearly. I have come up with a very rough idea as far as what I think the copy should contain. The picture is an example of what image I am trying to convey to the potential client. I am not a designer clearly. We specialise in treating difficult problems.
Size of the poster is 451mm x 741mm at 300dpi. We will then blow the image up to double this size which will be good enough resolution for the printing.

Target Market(s)

White collar professionals - male and female, active 20-50 range

Industry/Entity Type

Healthcare

Font styles to use
Sans Serif

Requirements
Nice to have
• Easy to read, polished, nice tie in to my logo colours

```html
<!DOCTYPE html>
<html lang="en">
<head>
<meta charset="utf-8">
<title>Corestride Physiotherapy – Injury Experts</title>
<link href="https://fonts.googleapis.com/css2?family=Montserrat:wght@600;700;800;900&family=Dosis:wght@500&display=swap" rel="stylesheet">
<style>
  :root {
    --green: #6cb33f;
    --green-deep: #2e8b3a;
    --green-lime: #9ccc3c;
    --ink: #3a3a3a;
    --paper: #ffffff;
    --photo-tone-a: #e7eaee;
    --photo-tone-b: #c9d0d8;
  }
  * { margin: 0; padding: 0; box-sizing: border-box; }
  html, body { width: 722px; height: 1200px; overflow: hidden; background: var(--paper); }
  .poster {
    position: relative;
    width: 722px;
    height: 1200px;
    overflow: hidden;
    background: var(--paper);
    font-family: "Montserrat", Arial, sans-serif;
    color: var(--ink);
  }
  .hero-photo {
    position: absolute;
    left: 408px; top: 500px;
    width: 314px; height: 700px;
    background: linear-gradient(180deg, var(--photo-tone-a) 0%, var(--photo-tone-b) 55%, var(--photo-tone-a) 100%);
    opacity: 0.55;
    border-radius: 140px 0 0 0;
  }
  .brand {
    position: absolute;
    left: 0; right: 0; top: 40px;
    display: flex;
    align-items: center;
    justify-content: center;
    gap: 16px;
  }
  .brand-dot {
    width: 70px; height: 70px;
    border-radius: 50%;
    background: var(--green);
    flex: none;
  }
  .brand-name {
    font-weight: 700;
    font-size: 25px;
    line-height: 1.15;
    letter-spacing: 1px;
    text-transform: uppercase;
    color: var(--ink);
  }
  .headline {
    position: absolute;
    left: 0; right: 0;
    text-align: center;
    font-weight: 900;
    line-height: 1;
    white-space: nowrap;
  }
  .headline span {
    display: inline-block;
    transform: scaleY(1.2);
    transform-origin: center;
  }
  .headline-injury {
    top: 150px;
    font-size: 158px;
  }
  .headline-injury span {
    background: linear-gradient(100deg, var(--green-deep) 0%, var(--green) 45%, var(--green-lime) 70%, var(--green) 100%);
    -webkit-background-clip: text;
    background-clip: text;
    color: transparent;
  }
  .headline-experts {
    top: 330px;
    font-size: 126px;
    color: var(--ink);
  }
  .tagline {
    position: absolute;
    left: 0; right: 0; top: 468px;
    text-align: center;
    font-weight: 800;
    font-size: 52px;
    letter-spacing: -1px;
    color: var(--ink);
    white-space: nowrap;
  }
  .tagline .accent { color: var(--green-deep); }
  .tagline .accent-bright { color: var(--green); }
  .since {
    position: absolute;
    left: 0; right: 0; top: 534px;
    text-align: center;
    font-weight: 800;
    font-size: 29px;
    line-height: 38px;
    color: var(--ink);
  }
  .services-bar {
    position: absolute;
    left: 48px; top: 630px;
    width: 633px; height: 64px;
    background: var(--green);
    color: var(--paper);
    font-family: "Dosis", Arial, sans-serif;
    font-weight: 500;
    font-size: 33px;
    display: flex;
    align-items: center;
    justify-content: center;
  }
  .services {
    position: absolute;
    left: 0; right: 0; top: 702px;
    list-style: none;
    text-align: center;
  }
  .services li {
    font-weight: 800;
    font-size: 40px;
    line-height: 69px;
    color: var(--ink);
  }
  .divider {
    position: absolute;
    left: 48px; top: 1052px;
    width: 627px; height: 2px;
    background: var(--green);
  }
  .contact {
    position: absolute;
    left: 0; right: 0; top: 1076px;
    list-style: none;
    text-align: center;
    color: var(--green);
    font-weight: 800;
    font-size: 26px;
    line-height: 37px;
  }
</style>
</head>
<body>
<main class="poster">
  <div class="hero-photo" role="img" aria-label="Faded photo of a footballer in a dark kit striking a ball"></div>

  <header class="brand">
    <span class="brand-dot"></span>
    <span class="brand-name">Corestride Physiotherapy<br>&amp; Sports Injury Clinic</span>
  </header>

  <h1>
    <span class="headline headline-injury"><span>INJURY</span></span>
    <span class="headline headline-experts"><span>EXPERTS</span></span>
  </h1>

  <p class="tagline"><span class="accent">TRUSTED</span> BY <span class="accent-bright">ATHLETES</span></p>
  <p class="since">SUCCESSFULLY TREATING DIFFICULT<br>INJURIES SINCE 1999</p>

  <div class="services-bar">Our complete range of services include</div>
  <ul class="services">
    <li>SPORTS PHYSIOTHERAPY</li>
    <li>CHIROPRACTIC</li>
    <li>MASSAGE</li>
    <li>PODIATRY</li>
    <li>EXERCISE PHYSIOLOGY</li>
  </ul>

  <div class="divider"></div>

  <ul class="contact">
    <li>TAKE LIFTS TO LEVEL 8</li>
    <li>8415 2290</li>
    <li>corestridephysio.com.au</li>
  </ul>
</main>
</body>
</html>
```